Property Management Company Business Cards

Need business cards for a property management company located in Michigan. We manage houses for clients all over the world. Young and modern company, looking for eye catching design. Please work with the attached logo.

Industry/Entity Type

Property Management

Requirements
Must have
• Need lines for address, telephone number, fax number, web site.

Also lines for name, and job title

```html
<!DOCTYPE html>
<html lang="en">
<head>
<meta charset="utf-8">
<title>Lakeshore Harbor Management – Business Card</title>
<link rel="stylesheet" href="https://fonts.googleapis.com/css2?family=Khand:wght@500;600&display=swap">
<style>
  :root {
    --page: #ffffff;
    --card-blue: #6683c4;
    --map-front: #5f79b6;
    --map-back: #8196cf;
    --ink: #1f1f26;
    --logo-ink: #2f3036;
  }
  * { margin: 0; padding: 0; box-sizing: border-box; }
  html, body {
    width: 1033px;
    height: 1200px;
    overflow: hidden;
    background: var(--page);
  }
  .sheet {
    position: relative;
    width: 1033px;
    height: 1200px;
    font-family: "Khand", "Arial Narrow", sans-serif;
    color: var(--ink);
  }
  .card {
    position: absolute;
    left: 23px;
    width: 986px;
    height: 567px;
    background: var(--card-blue);
    overflow: hidden;
  }
  .card--front { top: 15px; }
  .card--back { top: 607px; }

  .world-map {
    position: absolute;
  }
  .card--front .world-map {
    left: 10px; top: 8px; width: 966px; height: 555px;
    background: radial-gradient(ellipse at 50% 45%, var(--map-front) 0%, rgba(95,121,182,0.55) 55%, rgba(102,131,196,0) 80%);
  }
  .card--back .world-map {
    left: 10px; top: 15px; width: 966px; height: 520px;
    background: radial-gradient(ellipse at 50% 40%, var(--map-back) 0%, rgba(129,150,207,0.6) 50%, rgba(102,131,196,0) 80%);
  }

  .brand {
    position: absolute;
    left: 0; right: 0;
    top: 224px;
    display: flex;
    align-items: center;
    justify-content: center;
    gap: 22px;
  }
  .brand-mark {
    width: 96px; height: 96px;
    border-radius: 50%;
    background: var(--logo-ink);
    flex: none;
  }
  .brand-name {
    font-weight: 600;
    font-size: 62px;
    line-height: 1;
    letter-spacing: 0.5px;
    color: var(--logo-ink);
    text-transform: uppercase;
  }

  .employee {
    position: absolute;
    left: 26px;
    top: 42px;
    display: flex;
    align-items: baseline;
    gap: 14px;
    white-space: nowrap;
  }
  .employee-name {
    font-weight: 600;
    font-size: 64px;
    line-height: 1;
  }
  .employee-title {
    font-weight: 600;
    font-size: 28px;
    line-height: 1;
  }

  .contact {
    position: absolute;
    left: 27px;
    top: 268px;
    list-style: none;
    font-weight: 500;
    font-size: 30px;
    line-height: 47px;
  }
  .website {
    position: absolute;
    right: 22px;
    top: 409px;
    font-weight: 600;
    font-size: 29px;
    line-height: 47px;
  }
</style>
</head>
<body>
  <main class="sheet">
    <section class="card card--front">
      <div class="world-map" role="img" aria-label="Dotted world map pattern in a soft darker blue"></div>
      <div class="brand">
        <span class="brand-mark"></span>
        <span class="brand-name">Lakeshore Harbor Management</span>
      </div>
    </section>

    <section class="card card--back">
      <div class="world-map" role="img" aria-label="Faint world map silhouette in a lighter blue"></div>
      <div class="employee">
        <span class="employee-name">EMPLOYEE NAME</span>
        <span class="employee-title">EMPLOYEE TITLE</span>
      </div>
      <ul class="contact">
        <li>1420 Maple Ridge Drive</li>
        <li>Novi, MI 48375</li>
        <li>Phone: 555-010-4821</li>
        <li>Fax: 555-010-4822</li>
      </ul>
      <p class="website">www.lakeshoreharbor.com</p>
    </section>
  </main>
</body>
</html>
```